Business Card - BrightnookGoods.com

I need a business card that has my photo. It should say: My Pemavine store can be found on at the BrightnookGoods.com. Also find my links to Facebook, Youtube and Tiktok. (If this can be done graphically, then that's even better)

```html
<!DOCTYPE html>
<html lang="en">
<head>
<meta charset="utf-8">
<title>BrightnookGoods – Business Card</title>
<link href="https://fonts.googleapis.com/css2?family=Jost:wght@400;500;600&display=swap" rel="stylesheet">
<style>
  :root {
    --bg: #dde6f6;
    --card: #131313;
    --card-light: #262626;
    --ink: #b9b9b9;
    --ink-bright: #e6e6e6;
    --line: #8a8a8a;
    --strip: #ffffff;
    --photo-a: #6f6f6f;
    --photo-b: #c9a24a;
  }
  * { box-sizing: border-box; margin: 0; padding: 0; }
  html, body { width: 1200px; height: 900px; overflow: hidden; }
  body {
    background: var(--bg);
    font-family: "Jost", "Futura", sans-serif;
    position: relative;
  }
  .card {
    position: absolute;
    top: 300px;
    width: 520px;
    height: 297px;
    background: linear-gradient(125deg, var(--card) 0%, var(--card-light) 45%, var(--card) 75%);
    overflow: hidden;
    box-shadow: 0 6px 18px rgba(40, 60, 100, .25);
  }
  .card--front { left: 50px; }
  .card--back { left: 630px; }

  /* front */
  .side-strip {
    position: absolute; left: 0; top: 0;
    width: 62px; height: 228px;
    background: var(--strip);
  }
  .photo-frame {
    position: absolute; left: 30px; top: 22px;
    width: 150px; height: 140px;
    border: 1px solid var(--line);
  }
  .photo {
    position: absolute; left: 44px; top: 34px;
    width: 122px; height: 118px;
    background: linear-gradient(160deg, var(--photo-a) 0%, #9a9a9a 55%, var(--photo-b) 100%);
  }
  .front-text {
    position: absolute; left: 200px; top: 48px; right: 20px;
    text-align: center; color: var(--ink);
  }
  .brand-name { font-size: 29px; font-weight: 400; letter-spacing: .5px; line-height: 1.1; }
  .hours { font-size: 10px; color: var(--ink-bright); margin-top: 6px; font-weight: 500; }
  .store-line { font-size: 15px; margin-top: 18px; }
  .store-line--lead { font-size: 20px; font-weight: 600; margin-top: 2px; }
  .store-url { font-size: 12px; letter-spacing: 3px; margin-top: 4px; }
  .links {
    position: absolute; left: 24px; right: 20px; bottom: 20px;
    display: flex; align-items: center; gap: 18px;
    font-size: 8px; color: var(--ink);
  }
  .link { display: flex; align-items: center; gap: 6px; }
  .link-mark { width: 9px; height: 9px; background: var(--ink-bright); }
  .links-divider { width: 1px; height: 18px; background: var(--line); }
  .corner-shade {
    position: absolute; right: 0; bottom: 0;
    width: 0; height: 0;
    border-left: 40px solid transparent;
    border-bottom: 40px solid #0a0a0a;
  }

  /* back */
  .back-frame {
    position: absolute; inset: 18px;
    border: 1px solid var(--line);
    display: flex; flex-direction: column;
    align-items: center; justify-content: center;
    color: var(--ink);
  }
  .back-name { font-size: 40px; font-weight: 400; letter-spacing: .5px; }
  .back-url { font-size: 12px; letter-spacing: 3.5px; margin-top: 6px; }
</style>
</head>
<body>
  <section class="card card--front">
    <div class="side-strip"></div>
    <div class="photo-frame"></div>
    <div class="photo" role="img" aria-label="Portrait photo of the store owner"></div>
    <div class="front-text">
      <p class="brand-name">BrightnookGoods</p>
      <p class="hours">Open&nbsp; 09:00 am – 10:00 pm</p>
      <p class="store-line">My Pemavine store</p>
      <p class="store-line store-line--lead">can be found on at the</p>
      <p class="store-url">brightnookgoods.com</p>
    </div>
    <div class="links">
      <span class="link"><span class="link-mark"></span>www.friendspace.com/brightnook</span>
      <span class="link"><span class="link-mark"></span>www.vidstream.com/c/brightnook</span>
      <span class="links-divider"></span>
      <span class="link"><span class="link-mark"></span>www.loopclip.com/brightnook</span>
    </div>
    <div class="corner-shade"></div>
  </section>

  <section class="card card--back">
    <div class="back-frame">
      <p class="back-name">BrightnookGoods</p>
      <p class="back-url">brightnookgoods.com</p>
    </div>
  </section>
</body>
</html>
```